Design for schnapps bottle label "El Sendero"

Hi! On a small land lot we are producing our own Italian schnapps "Grappa". For the bottles we would like to modernize our current labes that you find below. The two cats looking at each other should remain, but updated and more modern. I am very much looking forward to your suggestions. Best, Tobias

Target Market(s)

Schnapps bottle label

Requirements
Must have
• Cats should resemble the cats that are decorating the house entry (see attached), however, should have a more modern appearance.

Text elements should remain: "Grappa", "El Sendero", "Legnoso", "[Vintage Year], "Raccolta No", "Vol %"
Should not have
• Current ornament can be used, replaced or deleted (whatever looks best)

```html
<!DOCTYPE html>
<html lang="it">
<head>
<meta charset="utf-8">
<title>Grappa Legnoso 2015 – El Sendero</title>
<link rel="stylesheet" href="https://fonts.googleapis.com/css2?family=Kaushan+Script&family=Questrial&display=block">
<style>
  :root {
    --paper-black: #141313;
    --paper-black-light: #232121;
    --copper: #c98758;
    --kraft: #c4916a;
    --kraft-light: #d2a27c;
    --kraft-dark: #b07c55;
    --ink: #1b1918;
    --white: #ffffff;
  }
  * { margin: 0; padding: 0; box-sizing: border-box; }
  html, body {
    width: 851px;
    height: 1200px;
    overflow: hidden;
    background: var(--paper-black);
  }
  .label {
    position: relative;
    width: 851px;
    height: 1200px;
    overflow: hidden;
    background:
      radial-gradient(ellipse at 30% 20%, var(--paper-black-light) 0%, transparent 55%),
      radial-gradient(ellipse at 75% 85%, var(--paper-black-light) 0%, transparent 50%),
      var(--paper-black);
  }
  .kraft-band {
    position: absolute;
    left: 0;
    top: 0;
    width: 851px;
    height: 1200px;
    z-index: 0;
  }
  .cats-illustration {
    position: absolute;
    left: 127px;
    top: 535px;
    width: 614px;
    height: 347px;
    border-radius: 50%;
    background: radial-gradient(ellipse at center, rgba(27,25,24,0.8) 0%, rgba(27,25,24,0.5) 55%, rgba(27,25,24,0) 72%);
    z-index: 1;
  }
  .script {
    position: absolute;
    font-family: "Kaushan Script", "Yellowtail", cursive;
    font-weight: 400;
    white-space: nowrap;
    line-height: 1;
    z-index: 2;
  }
  .title-grappa {
    left: 0;
    width: 851px;
    top: 120px;
    text-align: center;
    font-size: 190px;
    color: var(--copper);
    transform: rotate(-5deg);
  }
  .cuvee-name {
    left: 0;
    width: 851px;
    top: 400px;
    text-align: center;
    font-size: 84px;
    color: var(--white);
    transform: rotate(-7deg);
  }
  .connector-di {
    left: 390px;
    top: 578px;
    font-size: 60px;
    color: var(--white);
    transform: rotate(-8deg);
  }
  .producer-name {
    left: 0;
    width: 851px;
    top: 895px;
    text-align: center;
    font-size: 104px;
    color: var(--white);
    transform: rotate(-8deg);
  }
  .footer-info {
    position: absolute;
    top: 1118px;
    font-family: "Questrial", sans-serif;
    font-size: 38px;
    color: var(--copper);
    line-height: 1;
    z-index: 2;
  }
  .batch-number { left: 73px; }
  .alcohol-volume { right: 50px; }
</style>
</head>
<body>
<main class="label">
  <svg class="kraft-band" viewBox="0 0 851 1200" aria-hidden="true">
    <defs>
      <linearGradient id="kraftTone" x1="0" y1="0" x2="1" y2="1">
        <stop offset="0" stop-color="#b07c55"/>
        <stop offset="0.5" stop-color="#d2a27c"/>
        <stop offset="1" stop-color="#c4916a"/>
      </linearGradient>
    </defs>
    <polygon fill="url(#kraftTone)"
      points="0,585 120,575 300,548 330,545 520,520 680,500 851,478 851,830 700,845 520,868 360,885 200,905 0,935"/>
    <polygon fill="url(#kraftTone)" points="690,485 851,458 851,470 700,492"/>
    <polygon fill="url(#kraftTone)" points="0,945 130,938 120,950 0,958"/>
  </svg>

  <div class="cats-illustration" role="img" aria-label="Two black cat silhouettes with arched backs and curled tails facing each other"></div>

  <h1 class="script title-grappa">Grappa</h1>
  <p class="script cuvee-name">"Legnoso" 2015</p>
  <p class="script connector-di">di</p>
  <p class="script producer-name">El Sendero</p>

  <p class="footer-info batch-number">Raccolta No. 01</p>
  <p class="footer-info alcohol-volume">41.0%Vol.</p>
</main>
</body>
</html>
```